Corbel Path Advisory WordPress Design

Corbel Path Advisory is a consulting company that targets small business. We use our genius in the field to help small Business navigate information systems, in particular Tallybridge Solutions.

We are looking for a WordPress Design that is playful but intelligent for our web site. The design should plays off of our Corbel Logo and be informative. The attachments is of our logo variations that will be used in your design. It should be useful to describe the look and feel of the site we are looking to get.

The color of the website is not defined yet but should work well with our logo colors.

Regarding to the template and the way to display the home page. The menu should contain the following items which will each be its own page:
1. Home Page
2. Blog
-This needs to be a frame work to allow us to constantly add written articles and Video logs with Transcripts possibly in two sections.
3. What Corbel Does
-This will contain the company approach
4. Request a Corbel
-This will be a form to collect contact information
5. Contact Corbel
6. About Us

Please keep the SIMILAR airy/mythical design used in the logo.

Finally, we need a design that will have a normal view and a mobile view.

Target Market(s)

Corbel Path Advisory is a consulting company that targets small business.

Industry/Entity Type

Business Consultant

Requirements
Must have
• Regarding to the template and the way to display the home page. The menu should contain the following items which will each be its own page:
• 1. Home Page
• 2. Blog
• -This needs to be a frame work to allow us to constantly add written articles and Video logs with Transcripts possibly in two sections.
• 3. What Corbel Does
• -This will contain the company approach
• 4. Request a Corbel
• -This will be a form to collect contact information
• 5. Contact Corbel
• 6. About Us
• Mobile View
Nice to have
• Have a magical or mythical quality like the hands around the logo but not to playful.
Should not have
• Our slogan is "Corbel solutions that make business work!"

```html
<!DOCTYPE html>
<html lang="en">
<head>
<meta charset="utf-8">
<title>Corbel Path Advisory</title>
<link href="https://fonts.googleapis.com/css2?family=Open+Sans:wght@400;600;700&display=swap" rel="stylesheet">
<style>
:root{
  --blue:#1f5a9e;
  --blue-dark:#174a85;
  --navy:#1b4c88;
  --navy-deep:#143b6b;
  --orange:#f39200;
  --orange-light:#f9b233;
  --grey-text:#8a8a8a;
  --grey-band:#f3f3f3;
  --white:#ffffff;
}
*{margin:0;padding:0;box-sizing:border-box}
html,body{width:1200px;height:2280px;overflow:hidden}
body{font-family:"Open Sans",Arial,sans-serif;background:var(--white);color:#555;position:relative}

/* header + hero */
.hero{position:absolute;top:0;left:0;width:1200px;height:560px;
  background:radial-gradient(ellipse at 50% 40%,#ffffff 0%,#f1f3f5 55%,#dfe3e7 100%)}
.main-nav{position:absolute;top:18px;left:0;width:100%;display:flex;justify-content:center;align-items:center;gap:26px;
  font-size:11px;font-weight:700;letter-spacing:.6px;text-transform:uppercase;color:var(--orange)}
.main-nav a{text-decoration:none;color:var(--orange);padding:5px 10px}
.main-nav a.is-active{background:var(--orange);color:var(--white);border-radius:2px}
.main-nav svg{width:14px;height:14px}
.hero-brand{position:absolute;top:150px;left:0;width:100%;display:flex;justify-content:center;align-items:center;gap:34px}
.brand-dot{width:170px;height:170px;border-radius:50%;background:var(--blue)}
.brand-name{font-size:52px;font-weight:700;color:var(--blue);line-height:1.1;width:380px}
.hero-down{position:absolute;top:510px;left:582px;width:36px;height:20px}

/* what we do */
.about{position:absolute;top:560px;left:0;width:1200px;height:300px;background:var(--white);text-align:center}
.section-title{font-size:32px;font-weight:600;color:var(--blue)}
.about .section-title{margin-top:92px}
.title-rule{width:70px;height:3px;background:var(--orange);margin:12px auto 0}
.about p{width:880px;margin:22px auto 0;font-size:12.5px;line-height:21px;color:var(--grey-text)}

/* steps */
.steps{position:absolute;top:860px;left:0;width:1200px;height:220px;background:var(--grey-band);
  display:flex;justify-content:center;align-items:flex-start;padding-top:34px;gap:22px}
.step{width:170px;text-align:center}
.step-circle{width:110px;height:110px;border-radius:50%;border:3px solid var(--orange);background:var(--white);
  margin:0 auto;display:flex;align-items:center;justify-content:center}
.step-circle svg{width:56px;height:56px}
.step-label{margin-top:12px;font-size:15px;font-weight:700;color:var(--blue);line-height:19px}
.step-arrow{width:70px;height:110px;display:flex;align-items:center;justify-content:center}
.step-arrow svg{width:34px;height:60px}

/* orange band + cta */
.band{position:absolute;top:1080px;left:0;width:1200px;height:100px;
  background:linear-gradient(180deg,var(--orange-light) 0%,var(--orange) 55%,#f7c46b 100%)}
.cta{position:absolute;top:1180px;left:0;width:1200px;height:110px;background:var(--white);display:flex;justify-content:center;align-items:center}
.btn-outline{border:2px solid var(--orange);color:#333;font-size:11px;font-weight:700;letter-spacing:1px;padding:10px 40px;text-transform:uppercase}

/* request form */
.request{position:absolute;top:1290px;left:0;width:1200px;height:610px;
  background:linear-gradient(180deg,#4f8fd8 0%,#8bbbeb 40%,#d8e8f8 75%,#b9d4f0 100%)}
.request .section-title{position:absolute;top:50px;width:100%;text-align:center;color:var(--blue-dark)}
.request-form{position:absolute;top:130px;left:280px;width:640px;height:400px;background:rgba(255,255,255,.72);padding:24px}
.field-row{display:flex;gap:20px;margin-bottom:16px}
.field{flex:1;height:36px;background:var(--white);border:1px solid #d6dde6;font-size:11px;color:#999;padding:10px 12px}
.field-message{height:130px}
.captcha-row{display:flex;gap:20px;align-items:center;margin-bottom:18px}
.captcha-row .field{flex:1}
.captcha-box{width:200px;height:46px;background:linear-gradient(90deg,#eef2f6,#dfe6ee)}
.btn-submit{height:40px;background:var(--blue);color:var(--white);font-size:12px;font-weight:700;letter-spacing:1px;
  display:flex;align-items:center;justify-content:center}

/* footer */
.site-footer{position:absolute;top:1900px;left:0;width:1200px;height:320px;background:var(--navy);color:#dbe5f2}
.footer-contact{position:absolute;top:60px;left:150px;font-size:11px;line-height:19px}
.footer-contact strong{font-weight:700;color:var(--white)}
.social{display:flex;gap:12px;margin-top:12px}
.social span{width:14px;height:14px;border-radius:50%;background:#b7c9e2}
.footer-brand{position:absolute;top:70px;left:0;width:1200px;text-align:center}
.footer-brand .brand-dot{width:90px;height:90px;margin:0 auto;background:var(--orange)}
.footer-brand .brand-name{font-size:22px;color:var(--white);width:auto;margin-top:14px}
.recent-posts{position:absolute;top:60px;right:150px;text-align:right;font-size:11px;line-height:19px}
.recent-posts h3{color:var(--orange);font-size:16px;font-weight:600;margin-bottom:8px}
.footer-bar{position:absolute;top:2220px;left:0;width:1200px;height:60px;background:var(--navy-deep);
  color:#a9bcd6;font-size:10px;display:flex;align-items:center;justify-content:center;letter-spacing:.5px}
</style>
</head>
<body>

<header class="hero">
  <nav class="main-nav">
    <a class="is-active">Home</a>
    <a>Blog</a>
    <a>What Corbel Does</a>
    <a>Request a Corbel</a>
    <a>Contact Corbel</a>
    <a>About Us</a>
    <svg viewBox="0 0 14 14"><circle cx="6" cy="6" r="4.2" fill="none" stroke="#f39200" stroke-width="1.8"/><line x1="9" y1="9" x2="13" y2="13" stroke="#f39200" stroke-width="1.8"/></svg>
  </nav>
  <div class="hero-brand">
    <div class="brand-dot"></div>
    <div class="brand-name">Corbel Path Advisory</div>
  </div>
  <svg class="hero-down" viewBox="0 0 36 20"><polyline points="3,3 18,16 33,3" fill="none" stroke="#f39200" stroke-width="3"/></svg>
</header>

<section class="about">
  <h2 class="section-title">What Corbel Does</h2>
  <div class="title-rule"></div>
  <p>We work beside small business owners to untangle their information systems, shape clear processes and set up Tallybridge workspaces that people actually enjoy using. Our advisors listen first, map how your team already works, then build simple sites, libraries and workflows around it. Training, support and steady improvement follow, so your tools keep pace as the business grows and changes over time.</p>
</section>

<section class="steps">
  <div class="step">
    <div class="step-circle">
      <svg viewBox="0 0 56 56"><circle cx="28" cy="18" r="10" fill="#f39200"/><path d="M8 52 C8 36 48 36 48 52 Z" fill="#f39200"/></svg>
    </div>
    <div class="step-label">Small<br>Businessmen</div>
  </div>
  <div class="step-arrow"><svg viewBox="0 0 34 60"><polyline points="6,4 28,30 6,56" fill="none" stroke="#b5b5b5" stroke-width="2"/></svg></div>
  <div class="step">
    <div class="step-circle">
      <svg viewBox="0 0 56 56"><circle cx="28" cy="22" r="14" fill="none" stroke="#f39200" stroke-width="4"/><rect x="21" y="38" width="14" height="5" fill="#f39200"/><rect x="22" y="45" width="12" height="4" fill="#f39200"/></svg>
    </div>
    <div class="step-label">Our Corbel</div>
  </div>
  <div class="step-arrow"><svg viewBox="0 0 34 60"><polyline points="6,4 28,30 6,56" fill="none" stroke="#b5b5b5" stroke-width="2"/></svg></div>
  <div class="step">
    <div class="step-circle">
      <svg viewBox="0 0 56 56"><circle cx="22" cy="32" r="11" fill="none" stroke="#f39200" stroke-width="6" stroke-dasharray="5 3"/><circle cx="22" cy="32" r="4" fill="#f39200"/><circle cx="40" cy="16" r="7" fill="none" stroke="#f39200" stroke-width="5" stroke-dasharray="4 2.5"/></svg>
    </div>
    <div class="step-label">Corbel Solutions</div>
  </div>
  <div class="step-arrow"><svg viewBox="0 0 34 60"><polyline points="6,4 28,30 6,56" fill="none" stroke="#b5b5b5" stroke-width="2"/></svg></div>
  <div class="step">
    <div class="step-circle">
      <svg viewBox="0 0 56 56"><text x="28" y="38" text-anchor="middle" font-family="Open Sans,Arial,sans-serif" font-size="30" font-weight="700" fill="#f39200">$$</text></svg>
    </div>
    <div class="step-label">Business<br>Performance</div>
  </div>
</section>

<div class="band"></div>
<div class="cta"><span class="btn-outline">Learn More</span></div>

<section class="request" role="img" aria-label="Bright blue sky with soft white clouds behind the request form">
  <h2 class="section-title">Request a Corbel</h2>
  <form class="request-form">
    <div class="field-row"><div class="field">First Name</div><div class="field">Last Name</div></div>
    <div class="field-row"><div class="field">Email</div><div class="field">Phone</div></div>
    <div class="field-row"><div class="field field-message">Message</div></div>
    <div class="captcha-row"><div class="field">Enter Captcha</div><div class="captcha-box" role="img" aria-label="Captcha image"></div></div>
    <div class="btn-submit">SUBMIT</div>
  </form>
</section>

<footer class="site-footer">
  <div class="footer-contact">
    <strong>Corbel Path Advisory</strong><br>
    1420 Harbor Lane<br>
    Fairview, ST 00000<br>
    <strong>Email:</strong> hello@corbelpath.example<br>
    <strong>Phone:</strong> +1 (555) 014-2290<br>
    <strong>Fax:</strong> +1 (555) 014-2291
    <div class="social"><span></span><span></span><span></span></div>
  </div>
  <div class="footer-brand">
    <div class="brand-dot"></div>
    <div class="brand-name">Corbel Path Advisory</div>
  </div>
  <div class="recent-posts">
    <h3>Recent Posts</h3>
    Mapping workflows for small teams<br>
    Why intranets fail and how to fix<br>
    Video log: setting up libraries<br>
    Three quick wins for document control<br>
    Transcript: asking better questions
  </div>
</footer>
<div class="footer-bar">© 2024 CORBEL PATH ADVISORY. ALL RIGHTS RESERVED.</div>

</body>
</html>
```